Poster of Core Values & Motto

Create our core values poster and motto. Attached are our core values and our Motto. This poster represents both of our companies Tidy Pulp & CuraBinix.

Target Market(s)

Our team / employees

Industry/Entity Type

Shredding and Medical Waste

Colors
59FF00
82FF00
B8FF75
E3FFCB
F4FFEA
EB3D1F
EC4F4E
F09395
F8D3D4
FCEDEE

Requirements
Must have
• Include both companies logos

```html
<!DOCTYPE html>
<html lang="en">
<head>
<meta charset="utf-8">
<title>Core Values Poster — Tidy Pulp &amp; CuraBinix</title>
<link rel="stylesheet" href="https://fonts.googleapis.com/css2?family=Nunito:wght@600;700;800&display=swap">
<style>
  :root {
    --green: #2eaa4f;
    --green-text: #2ea84f;
    --ribbon: #de5b55;
    --ribbon-text: #de5b55;
    --white: #ffffff;
    --ink: #333333;
    --muted: #555555;
    --paper: #ffffff;
  }
  * { margin: 0; padding: 0; box-sizing: border-box; }
  html, body { width: 848px; height: 1200px; overflow: hidden; background: var(--paper); }
  .poster {
    position: relative;
    width: 848px;
    height: 1200px;
    background: var(--paper);
    font-family: "Nunito", "Varela Round", sans-serif;
    overflow: hidden;
  }
  .masthead {
    position: absolute;
    left: 0; top: 0;
    width: 848px; height: 168px;
    background: var(--green);
    display: flex; align-items: center; justify-content: center;
  }
  .masthead__title {
    color: var(--white);
    font-weight: 800;
    font-size: 62px;
    letter-spacing: 0.5px;
    line-height: 1;
  }
  .motto {
    position: absolute;
    top: 174px; left: 0; width: 848px;
    text-align: center;
    color: var(--green-text);
    font-weight: 700;
    font-size: 30px;
  }
  .value {
    position: absolute;
    left: 0; width: 848px;
    text-align: center;
  }
  .value__ribbon {
    position: relative;
    width: 848px; height: 48px;
  }
  .value__ribbon svg { position: absolute; left: 0; top: 0; }
  .value__name {
    position: relative;
    line-height: 48px;
    color: var(--white);
    font-weight: 800;
    font-size: 43px;
  }
  .value__line {
    margin-top: 2px;
    color: var(--ribbon-text);
    font-weight: 700;
    font-size: 29.5px;
    line-height: 38px;
    white-space: nowrap;
  }
  .brand {
    position: absolute;
    display: flex; align-items: center; gap: 12px;
    font-weight: 800;
    font-size: 34px;
    line-height: 1;
  }
  .brand__dot { width: 44px; height: 44px; border-radius: 50%; }
  .brand--pulp { left: 88px; top: 1046px; color: var(--green); }
  .brand--pulp .brand__dot { background: var(--green); }
  .brand--bin { left: 516px; top: 1046px; color: var(--ribbon); }
  .brand--bin .brand__dot { background: var(--ribbon); }
  .fineprint {
    position: absolute;
    left: 40px; top: 1128px; width: 768px;
    text-align: center;
    color: var(--muted);
    font-family: "Nunito", sans-serif;
    font-weight: 600;
    font-size: 11px;
    line-height: 16px;
  }
</style>
</head>
<body>
<main class="poster">
  <header class="masthead">
    <h1 class="masthead__title">Purpose/Cause/Passion</h1>
  </header>
  <p class="motto">Remind people what great service looks like</p>

  <section class="value" style="top:279px">
    <div class="value__ribbon">
      <svg width="848" height="48" viewBox="0 0 848 48" aria-hidden="true"><polygon points="16,0 832,0 806,24 832,48 16,48 42,24" fill="var(--ribbon)"/></svg>
      <h2 class="value__name">Synergy/Teamwork</h2>
    </div>
    <p class="value__line">Get It Done Attitude with Humble confidence</p>
  </section>

  <section class="value" style="top:401px">
    <div class="value__ribbon">
      <svg width="848" height="48" viewBox="0 0 848 48" aria-hidden="true"><polygon points="16,0 832,0 806,24 832,48 16,48 42,24" fill="var(--ribbon)"/></svg>
      <h2 class="value__name">Exellance</h2>
    </div>
    <p class="value__line">Exceed with a smile</p>
  </section>

  <section class="value" style="top:526px">
    <div class="value__ribbon">
      <svg width="848" height="48" viewBox="0 0 848 48" aria-hidden="true"><polygon points="16,0 832,0 806,24 832,48 16,48 42,24" fill="var(--ribbon)"/></svg>
      <h2 class="value__name">Efficient</h2>
    </div>
    <p class="value__line">On-Time, sence of urgency, always trying to improve</p>
  </section>

  <section class="value" style="top:650px">
    <div class="value__ribbon">
      <svg width="848" height="48" viewBox="0 0 848 48" aria-hidden="true"><polygon points="16,0 832,0 806,24 832,48 16,48 42,24" fill="var(--ribbon)"/></svg>
      <h2 class="value__name">Safe and Secure</h2>
    </div>
    <p class="value__line">We are just as secure as an armored truck with money</p>
  </section>

  <section class="value" style="top:774px">
    <div class="value__ribbon">
      <svg width="848" height="48" viewBox="0 0 848 48" aria-hidden="true"><polygon points="16,0 832,0 806,24 832,48 16,48 42,24" fill="var(--ribbon)"/></svg>
      <h2 class="value__name">Honesty/Integrity</h2>
    </div>
    <p class="value__line">Do the right thing</p>
  </section>

  <section class="value" style="top:897px">
    <div class="value__ribbon">
      <svg width="848" height="48" viewBox="0 0 848 48" aria-hidden="true"><polygon points="16,0 832,0 806,24 832,48 16,48 42,24" fill="var(--ribbon)"/></svg>
      <h2 class="value__name">Dependable</h2>
    </div>
    <p class="value__line">Do what you say you will do</p>
  </section>

  <div class="brand brand--pulp"><span class="brand__dot"></span><span>Tidy Pulp</span></div>
  <div class="brand brand--bin"><span class="brand__dot"></span><span>CuraBinix</span></div>

  <p class="fineprint">Lorem ipsum dolor sit amet, consectetuer adipiscing elit, sed diam nonummy nibh euismod tincidunt ut laoreet dolore magna aliquam erat volutpat. Ut wisi enim ad minim veniam, quis nostrud exerci tation ullamcorper suscipit lobortis nisl ut aliquip ex</p>
</main>
</body>
</html>
```